Web Design needed for logo design project

I am needing an interactive website for TC. Tandem Care Management is a nationwide company that combines the front desk administrative operation within Professional offices (Dental, Chiropractic, Optometry). I am needing a website designed that will provide information for potential new clients that are interested in joining our company to provide to them administrative support. I need a design for the marketing material within the folder, I will add content later. I am looking for clean crisp professional. No dancing teeth, hearts, or EKG signals please. We need it to appeal to 27-40 years old professionals. The professions are equally divided at 50/50 female to male. I already have a logo, it will be attached.
Updates

Target Market(s)

We need it to appeal to 27-40 years old professionals. The professions are equally divided at 50/50 female to male. I already have a logo, it will be attached.

Industry/Entity Type

Marketing

Requirements
Must have
• Needs to be in Word Press. It must have scalability to various screen sizes (Monitor, Phone screen, IPad, etc). Must have a customer portal capability, so professionals can access their information through a portal on the website. Have the capability to run a practice calculator or view a video requiring that it captures the visitors information so I can contact them regarding their interest in the site. Needs to have links to social media.

```html
<!DOCTYPE html>
<html lang="en">
<head>
<meta charset="utf-8">
<title>Tandem Care Management – Book a Consultation</title>
<link href="https://fonts.googleapis.com/css2?family=Open+Sans:wght@400;600;700&family=Noto+Serif:ital@1&display=swap" rel="stylesheet">
<style>
:root{
  --sky-1:#c9eef3;--sky-2:#e9f8fa;--white:#ffffff;
  --ink:#3a3a3a;--muted:#6b6b6b;--navy:#1d5f8a;--teal:#1aa3a8;
  --pink:#d0245c;--line:#dcdcdc;--field:#e9e9e9;--cal-head:#3c4b5b;
  --cal-days:#9aa3aa;--cell-off:#f3f3f3;--note:#efefef;
}
*{box-sizing:border-box;margin:0;padding:0}
html,body{width:1200px;height:973px;overflow:hidden}
body{font-family:"Open Sans",Arial,sans-serif;color:var(--ink);
  background:linear-gradient(160deg,var(--sky-2) 0%,var(--sky-1) 45%,var(--sky-2) 100%);position:relative}
.abs{position:absolute}
.brand{left:171px;top:26px;display:flex;align-items:center;gap:12px}
.brand-mark{width:34px;height:34px;background:var(--navy)}
.brand-name{font-size:21px;font-weight:600;color:var(--navy);letter-spacing:.5px;line-height:1.1}
.contact{right:185px;top:38px;text-align:right;font-size:14px;color:var(--ink);line-height:27px}
.contact b{color:var(--teal);font-weight:600}
.contact svg{vertical-align:-2px;margin-left:6px}
.frame{left:166px;top:112px;width:880px;height:870px;background:rgba(255,255,255,.45);border:4px solid rgba(255,255,255,.8)}
.page{left:182px;top:208px;width:840px;height:765px;background:var(--white)}
.nav{left:170px;top:115px;width:871px;height:95px;background:var(--white);border-bottom:1px solid var(--line)}
.tab{position:absolute;height:42px;top:4px;display:flex;align-items:center;justify-content:center;font-size:14px;font-weight:600;color:#2f3b45;background:linear-gradient(#fff,#eeeeee);border:1px solid var(--line)}
.tab.active{color:var(--pink);background:#fff;border-bottom-color:#fff}
.hero{left:182px;top:210px;width:840px;height:123px;background:linear-gradient(90deg,#c1434f 0%,#7fa6c6 22%,#4d86b6 45%,#2f74ad 100%)}
.hero-text{left:712px;top:244px;font-family:"Noto Serif",Georgia,serif;font-style:italic;color:#fff;font-size:18px;line-height:29px}
h1{position:absolute;left:191px;top:370px;font-size:22px;font-weight:400;color:#2b2b2b}
.label{font-size:14.5px;color:#2b2b2b}
.field{background:var(--field);border:1px solid #d2d2d2}
.select{left:191px;top:444px;width:218px;height:28px;font-size:14px;padding:4px 8px;color:#444;background:linear-gradient(#f2f2f2,#dedede)}
.select svg{position:absolute;right:8px;top:11px}
.btn{left:191px;top:677px;width:159px;height:25px;background:var(--pink);color:#fff;font-weight:700;font-size:13.5px;line-height:24px;text-align:center;border-bottom:3px solid #8e1238}
.cal{left:470px;top:469px;width:202px}
.cal-head{height:40px;background:var(--cal-head);color:#fff;font-weight:700;font-size:14.5px;display:flex;align-items:center;justify-content:center;gap:8px;border-radius:3px 3px 0 0}
.cal-grid{display:grid;grid-template-columns:repeat(7,26px);gap:3px;margin-top:2px}
.dow{background:var(--cal-days);color:#fff;font-weight:700;font-size:12px;text-align:center;height:23px;line-height:23px}
.day{height:34px;line-height:34px;text-align:center;font-size:13px;color:#b3b3b3;background:var(--cell-off);border:1px solid #e4e4e4}
.day.open{color:#333;background:#e2e2e2;font-weight:600}
.day.pick{color:#fff;background:var(--teal);font-weight:700}
.legend{left:470px;top:728px;font-family:"Noto Serif",Georgia,serif;font-style:italic;font-size:13.5px;color:var(--muted);display:flex;gap:30px}
.legend i{display:inline-block;width:9px;height:9px;margin-right:4px}
.note{left:191px;top:787px;width:540px;height:131px;background:var(--note);border:1px solid #d8d8d8;padding:22px 24px 0 57px;font-size:14px;line-height:25px;color:var(--muted)}
.note svg{position:absolute;left:20px;top:26px}
.side{left:752px;top:398px;width:270px}
.side a{display:block;height:42px;line-height:42px;padding-left:23px;border-bottom:1px solid #e3e3e3;font-family:"Noto Serif",Georgia,serif;font-style:italic;font-size:15.5px;color:var(--teal);text-decoration:none}
.side a:before{content:"•";margin-right:10px}
.feed{left:778px;top:668px;width:205px;height:305px;border:1px solid #cfcfcf;background:#fff;overflow:hidden}
.feed-title{height:37px;padding:0 10px;display:flex;justify-content:space-between;align-items:center;font-weight:600;font-size:14px;border-bottom:1px solid #ddd;color:#333}
.feed-dot{width:20px;height:20px;border-radius:50%;background:#3b5998}
.login{display:flex;gap:8px;padding:8px 6px;font-size:11px;color:#555;line-height:13px}
.login span.b{background:#4a66a0;color:#fff;font-weight:700;padding:3px 7px;height:21px}
.item{display:flex;gap:7px;padding:6px;border-top:1px solid #eee;font-size:11px;line-height:13px}
.thumb{width:30px;height:30px;flex:none;background:#555}
.item b{color:#3b5998;font-weight:700}
.item small{display:block;color:#888;font-size:10.5px}
</style>
</head>
<body>
<div class="abs frame"></div>
<div class="abs page"></div>

<div class="abs brand"><div class="brand-mark"></div><div class="brand-name">Tandem Care Management</div></div>

<div class="abs contact">
  Call us directly: <b>1-800-555-0142</b>
  <svg width="10" height="14" viewBox="0 0 10 14"><rect x="1" y="1" width="8" height="12" rx="1.5" fill="none" stroke="#555" stroke-width="1.4"/></svg><br>
  18 Linden Court, Fairview <b>View Location</b>
  <svg width="10" height="14" viewBox="0 0 10 14"><path d="M5 13C2 8 1 6.5 1 5a4 4 0 0 1 8 0c0 1.5-1 3-4 8z" fill="#555"/><circle cx="5" cy="5" r="1.5" fill="#fff"/></svg>
</div>

<nav class="abs nav">
  <span class="tab" style="left:2px;width:122px">Homepage</span>
  <span class="tab" style="left:128px;width:104px">About us</span>
  <span class="tab" style="left:236px;width:160px">Our Services</span>
  <span class="tab" style="left:400px;width:132px">Client Portal</span>
  <span class="tab active" style="left:536px;width:128px">Consultation</span>
  <span class="tab" style="left:668px;width:118px">Locations</span>
  <span class="tab" style="left:2px;top:50px;width:90px">Pages</span>
</nav>

<div class="abs hero" role="img" aria-label="Photo of a bright professional office front desk with staff at work"></div>
<div class="abs hero-text">At Tandem Care...<br>&nbsp;&nbsp;&nbsp;&nbsp;your front desk, "handled with care"</div>

<h1>Book a Consultation online:</h1>

<div class="abs label" style="left:191px;top:416px">Choose your practice type:</div>
<div class="abs field select">Dental Practice
  <svg width="8" height="5" viewBox="0 0 8 5"><path d="M0 0h8L4 5z" fill="#888"/></svg></div>
<div class="abs label" style="left:191px;top:496px">Your full name:</div>
<div class="abs field" style="left:191px;top:525px;width:218px;height:35px"></div>
<div class="abs" style="left:198px;top:533px;width:1px;height:18px;background:#333"></div>
<div class="abs label" style="left:191px;top:582px">Your email address:</div>
<div class="abs field" style="left:191px;top:610px;width:218px;height:34px"></div>
<div class="abs btn">BOOK A CALL</div>

<div class="abs label" style="left:469px;top:416px;width:200px;line-height:24px">Choose a date for your consultation:</div>

<div class="abs cal">
  <div class="cal-head">
    <svg width="10" height="10"><circle cx="5" cy="5" r="4" fill="#8ea0b0"/></svg>
    DECEMBER 2014
    <svg width="10" height="10"><circle cx="5" cy="5" r="4" fill="#fff"/></svg>
  </div>
  <div class="cal-grid">
    <div class="dow">M</div><div class="dow">T</div><div class="dow">W</div><div class="dow">T</div><div class="dow">F</div><div class="dow">S</div><div class="dow">S</div>
    <div class="day">1</div><div class="day">2</div><div class="day">3</div><div class="day">4</div><div class="day">5</div><div class="day">6</div><div class="day">7</div>
    <div class="day">8</div><div class="day">9</div><div class="day">10</div><div class="day">11</div><div class="day">12</div><div class="day">13</div><div class="day">14</div>
    <div class="day">15</div><div class="day">16</div><div class="day">17</div><div class="day">18</div><div class="day">19</div><div class="day">20</div><div class="day">21</div>
    <div class="day">22</div><div class="day">23</div><div class="day">24</div><div class="day">25</div><div class="day">26</div><div class="day">27</div><div class="day">28</div>
    <div class="day pick">29</div><div class="day open">30</div><div class="day open">31</div><div class="day">1</div><div class="day">2</div><div class="day">3</div><div class="day">4</div>
  </div>
</div>
<div class="abs legend">
  <span><i style="background:var(--teal)"></i>your selection</span>
  <span style="line-height:14px"><i style="border:1px solid #bbb"></i>not<br>available</span>
</div>

<div class="abs note">
  <svg width="20" height="18" viewBox="0 0 20 18"><path d="M10 1L19 17H1z" fill="#666"/><rect x="9" y="6" width="2" height="6" fill="#fff"/><rect x="9" y="13.5" width="2" height="2" fill="#fff"/></svg>
  Please note that this is not a signed agreement, but only a request for a consultation. We will contact you to confirm shortly after. Thank you! By clicking the "Book a Call" button you agree to the Terms &amp; Conditions below.
</div>

<div class="abs side">
  <a>Practice Calculator</a>
  <a>Watch Our Video</a>
  <a>Our History</a>
  <a>Dental, Chiro &amp; Optometry</a>
  <a style="border-bottom:none">Why partner with us?</a>
</div>

<div class="abs feed">
  <div class="feed-title">Socialfeed activity <span class="feed-dot"></span></div>
  <div class="login"><span class="b">Login</span><span>You need to be logged into see your friends' activity.</span></div>
  <div class="item"><div class="thumb"></div><div><b>Retro gadgets shrunk down to pocket size -- Techwire</b><small>714 people shared this.</small></div></div>
  <div class="item"><div class="thumb"></div><div><b>Nap breaks may be the new key to focus -- Techwire</b><small>422 people shared this.</small></div></div>
  <div class="item"><div class="thumb"></div><div><b>Quizbot wins it all, humans still do other things -- Techwire</b><small>668 people shared this.</small></div></div>
  <div class="item"><div class="thumb"></div><div><b>Pagewell Books files for bankruptcy, will close 30 stores -- Techwire</b><small>231 people shared this.</small></div></div>
</div>
</body>
</html>
```